Lorena Vex Wigs " Styling Foam"

I need a label created for my product . The bottle size is 50ml so it must be designed to fit that size bottle. I will post my logo and examples of my bottle size. I want the label design to be simple and cute. ill also add pictures of my website, so you can get ideas from there. The bottle is white so I want the main colors to be white and pink. All colors on the label must match my logo. I love glitter as well.

I know for sure I want my logo big, and I want "Styling Foam'',
then under styling foam I would like " Medium Hold" in a different front. be very creative.

Then under that I would like it to say " No Alcohol , Saulfate or Paraben

please make sure on the label in the front it has "NET: 7.0 oz / 200g" so people know what size it is.

I would like a glitter border on the label.

I also want the back of the label to have directions.

And ingredients list too . Very small not too big at all.

Target Market(s)

My target market is woman of all ages .. but mainly woman from ages 26-65

Industry/Entity Type

Hair And Beauty

Font styles to use
Serif
Sans Serif
Decorative
Script

Colors
e667a6
eda3c7
f9d9e8
e34297

Requirements
Must have
• The project must match the colors of my logo, it must have a nice pretty glitter border . It must be simple and clean . But still stylish ! I don’t want everything after my logo to be in the same font . Have fun with this design, be creative. My logo and “ Styling Foam” must be the two centerpiece!
Nice to have
• It will be nice to have different fonts! And nice to have all the colors that match my logo
Must be expensive looking !!
Very eye catching!
Should not have
• Do not add colors that my logo doesn’t have !!!!
I don’t want it to look too plain and boring ! I want it to be classy and expensive looking !

```html
<!DOCTYPE html>
<html lang="en">
<head>
<meta charset="utf-8">
<title>Lorena Vex Wigs – Styling Foam Labels</title>
<link rel="stylesheet" href="https://fonts.googleapis.com/css2?family=Permanent+Marker&family=Oswald:wght@500&family=Great+Vibes&family=Josefin+Sans:wght@200&family=Montserrat:wght@700&display=swap">
<style>
  :root {
    --backdrop: #667aa3;
    --label-white: #ffffff;
    --pink-deep: #e34297;
    --pink-main: #e667a6;
    --pink-soft: #eda3c7;
    --pink-blush: #f9d9e8;
    --ink-grey: #5a5a5a;
    --ink-dark: #2b2b2b;
  }
  html, body {
    margin: 0;
    padding: 0;
    width: 1200px;
    height: 975px;
    overflow: hidden;
    background: var(--backdrop);
  }
  .canvas { position: relative; width: 1200px; height: 975px; }
  .label {
    position: absolute;
    top: 165px;
    width: 340px;
    height: 645px;
    background: var(--label-white);
    overflow: hidden;
    box-shadow: 0 6px 18px rgba(0,0,0,0.18);
  }
  .label--classic { left: 185px; }
  .label--wave { left: 675px; }

  .decor { position: absolute; }
  .decor--side {
    top: 0;
    right: 0;
    width: 125px;
    height: 480px;
    border-bottom-left-radius: 125px 240px;
    border-top-left-radius: 125px 240px;
    background: linear-gradient(90deg, var(--pink-soft), var(--pink-main) 55%, var(--pink-deep));
  }
  .decor--top {
    top: 0; left: 0; right: 0;
    height: 90px;
    background: linear-gradient(180deg, var(--pink-deep), var(--pink-main) 60%, var(--pink-soft));
  }
  .decor--bottom {
    bottom: 0; left: 0; right: 0;
    height: 120px;
    background: linear-gradient(180deg, var(--pink-blush), var(--pink-soft) 35%, var(--pink-main));
  }

  .text { position: absolute; left: 0; right: 0; text-align: center; margin: 0; }
  .brand-name {
    font-family: "Oswald", sans-serif;
    font-weight: 500;
    color: var(--ink-grey);
    font-size: 30px;
    line-height: 1.05;
    letter-spacing: 2px;
    text-transform: uppercase;
  }
  .label--classic .brand-name { top: 120px; left: 10px; right: 130px; }
  .label--wave .brand-name { top: 148px; }

  .title-brush {
    top: 372px;
    left: 10px;
    right: 105px;
    font-family: "Permanent Marker", "Comic Sans MS", cursive;
    font-weight: 400;
    color: var(--pink-deep);
    font-size: 40px;
    line-height: 1.05;
  }
  .hold {
    font-family: "Oswald", sans-serif;
    font-weight: 500;
    color: var(--ink-grey);
    font-size: 34px;
    letter-spacing: 0.5px;
    line-height: 1.2;
  }
  .label--classic .hold { top: 492px; left: 10px; right: 90px; }
  .label--wave .hold { top: 420px; }

  .title-script {
    top: 250px;
    left: 28px;
    font-family: "Great Vibes", cursive;
    font-weight: 400;
    color: var(--pink-main);
    font-size: 80px;
    text-align: left;
    line-height: 1;
  }
  .title-thin {
    top: 330px;
    right: 30px;
    left: auto;
    font-family: "Josefin Sans", sans-serif;
    font-weight: 200;
    font-size: 38px;
    color: var(--ink-dark);
    letter-spacing: 4px;
  }
  .net { font-family: "Montserrat", sans-serif; font-weight: 700; font-size: 13px; }
  .label--classic .net { top: 600px; left: 10px; right: 90px; color: var(--ink-dark); }
  .label--wave .net { top: 603px; color: var(--label-white); font-size: 14px; }

  .free-from { position: absolute; display: flex; gap: 8px; }
  .label--classic .free-from { top: 552px; left: 92px; }
  .label--wave .free-from { top: 478px; left: 128px; }
  .free-from svg { width: 38px; height: 38px; }
</style>
</head>
<body>
<main class="canvas">

  <section class="label label--classic" aria-label="Styling foam front label, brush title">
    <div class="decor decor--side" role="img" aria-label="Layered pink swirl decoration along the right edge"></div>
    <p class="text brand-name">Lorena Vex<br>Wigs</p>
    <h1 class="text title-brush">STYLING<br>FOAM</h1>
    <p class="text hold">MEDIUM HOLD</p>
    <div class="free-from" role="img" aria-label="No alcohol, no sulfate or paraben">
      <svg viewBox="0 0 40 40"><circle cx="20" cy="20" r="18" fill="var(--pink-main)"/><rect x="16" y="10" width="8" height="20" rx="2" fill="none" stroke="#fff" stroke-width="1.8"/><line x1="9" y1="31" x2="31" y2="9" stroke="#fff" stroke-width="1.8"/></svg>
      <svg viewBox="0 0 40 40"><circle cx="20" cy="20" r="18" fill="var(--pink-main)"/><path d="M16 10 L24 10 M18 10 L18 18 L12 29 L28 29 L22 18 L22 10" fill="none" stroke="#fff" stroke-width="1.8"/><line x1="9" y1="31" x2="31" y2="9" stroke="#fff" stroke-width="1.8"/></svg>
    </div>
    <p class="text net">NET: 7.0 oz / 200g</p>
  </section>

  <section class="label label--wave" aria-label="Styling foam front label, script title">
    <div class="decor decor--top" role="img" aria-label="Pink wave band decoration across the top"></div>
    <div class="decor decor--bottom" role="img" aria-label="Pink wave band decoration across the bottom"></div>
    <p class="text brand-name">Lorena Vex<br>Wigs</p>
    <h1 class="text title-script">Styling</h1>
    <p class="text title-thin">FOAM</p>
    <p class="text hold">MEDIUM HOLD</p>
    <div class="free-from" role="img" aria-label="No alcohol, no sulfate or paraben">
      <svg viewBox="0 0 40 40"><circle cx="20" cy="20" r="18" fill="none" stroke="var(--ink-grey)" stroke-width="1.5"/><rect x="16" y="10" width="8" height="20" rx="2" fill="none" stroke="var(--ink-grey)" stroke-width="1.5"/><line x1="9" y1="31" x2="31" y2="9" stroke="var(--ink-grey)" stroke-width="1.5"/></svg>
      <svg viewBox="0 0 40 40"><circle cx="20" cy="20" r="18" fill="none" stroke="var(--ink-grey)" stroke-width="1.5"/><path d="M16 10 L24 10 M18 10 L18 18 L12 29 L28 29 L22 18 L22 10" fill="none" stroke="var(--ink-grey)" stroke-width="1.5"/><line x1="9" y1="31" x2="31" y2="9" stroke="var(--ink-grey)" stroke-width="1.5"/></svg>
    </div>
    <p class="text net">NET: 7.0 oz / 200g</p>
  </section>

</main>
</body>
</html>
```